Adventure Business Cards

Please check out our website for style
Vertical card
Details:
Side 1
Logo
Business name: Kestrel Point Wildland Tours
Name: Colin Warbeck
Role: Director
Email: info@kestrelpointtours.com
Address: PO Box 71, Marlin Cove NSW 2471
Phone: +61 2 5550 1847
Web address: www.kestrelpointtours.com
Side 2
Taking pictures?
A Friendwall and Pixlane logo
Tag us in your pictures with
#kpwildtours
@kpwildtours
www.kestrelpointtours.com
Details:
Side 1
Logo
Name: Colin Warbeck
Role: Director
Phone: +61 2 5550 1847
Side 2
Taking pictures?
#kpwildtours
@kpwildtours

```html
<!DOCTYPE html>
<html lang="en">
<head>
<meta charset="utf-8">
<title>Kestrel Point Wildland Tours – Business Cards</title>
<link href="https://fonts.googleapis.com/css2?family=Open+Sans:wght@400;600;700;800&display=swap" rel="stylesheet">
<style>
  :root {
    --bg: #e9e6e1;
    --card-black: #1c1c1c;
    --white: #ffffff;
    --orange: #f39a1e;
    --yellow: #f7b733;
    --blue: #2a8fd0;
    --blue-dark: #1b6aa8;
    --text-light: #f2f2f2;
    --text-muted: #c9c9c9;
  }
  * { box-sizing: border-box; margin: 0; padding: 0; }
  html, body { width: 1200px; height: 950px; overflow: hidden; }
  body {
    background: var(--bg);
    font-family: "Open Sans", Arial, sans-serif;
    position: relative;
  }
  .card {
    position: absolute;
    top: 165px;
    width: 380px;
    height: 620px;
    border-radius: 6px;
    overflow: hidden;
    box-shadow: 0 10px 30px rgba(0,0,0,0.18);
  }
  .card--front { left: 170px; background: var(--white); }
  .card--back  { left: 650px; background: var(--card-black); }

  .front-bands { position: absolute; inset: 0; }

  .holder {
    position: absolute;
    top: 42px;
    left: 36px;
  }
  .holder__name {
    color: var(--orange);
    font-weight: 800;
    font-size: 26px;
    letter-spacing: 0.5px;
    text-transform: uppercase;
  }
  .holder__role {
    color: var(--blue);
    font-weight: 600;
    font-size: 13px;
    letter-spacing: 1px;
    text-transform: uppercase;
    text-align: right;
    margin-top: -2px;
  }
  .holder__phone {
    color: var(--text-light);
    font-size: 20px;
    margin-top: 12px;
  }

  .brand {
    position: absolute;
    left: 50%;
    transform: translate(-50%, -50%);
    display: flex;
    flex-direction: column;
    align-items: center;
    gap: 10px;
    width: 240px;
    text-align: center;
  }
  .card--front .brand { top: 300px; }
  .card--back .brand  { top: 260px; }
  .brand__dot {
    width: 76px;
    height: 76px;
    border-radius: 50%;
    background: var(--blue);
  }
  .card--back .brand__dot { width: 88px; height: 88px; }
  .brand__name {
    font-weight: 800;
    font-size: 22px;
    line-height: 1.2;
    text-transform: uppercase;
    letter-spacing: 0.5px;
  }
  .card--front .brand__name { color: var(--card-black); }
  .card--back .brand__name  { color: var(--white); }

  .contact {
    position: absolute;
    left: 36px;
    bottom: 30px;
    color: var(--text-light);
    font-size: 16px;
    line-height: 1.6;
  }
  .contact__label { color: var(--orange); font-weight: 700; }

  .social {
    position: absolute;
    left: 0;
    right: 0;
    bottom: 60px;
    display: flex;
    flex-direction: column;
    align-items: center;
    gap: 10px;
    color: var(--text-light);
  }
  .social__networks {
    display: flex;
    gap: 16px;
    font-size: 13px;
    font-weight: 600;
    color: var(--text-muted);
  }
  .social__handle { font-size: 17px; }
</style>
</head>
<body>

  <section class="card card--front" aria-label="Business card front">
    <svg class="front-bands" width="380" height="620" viewBox="0 0 380 620" aria-hidden="true">
      <defs>
        <linearGradient id="band-blue" x1="0" y1="0" x2="1" y2="0">
          <stop offset="0" stop-color="#1b6aa8"/>
          <stop offset="0.5" stop-color="#5bb6ea"/>
          <stop offset="1" stop-color="#1b6aa8"/>
        </linearGradient>
      </defs>
      <polygon points="0,0 380,0 380,140 0,220" fill="#1c1c1c"/>
      <polygon points="0,220 380,140 380,158 0,238" fill="url(#band-blue)"/>
      <polygon points="0,238 380,158 380,172 0,252" fill="#f7b733"/>
      <polygon points="0,440 380,360 380,374 0,454" fill="#f7b733"/>
      <polygon points="0,454 380,374 380,392 0,472" fill="url(#band-blue)"/>
      <polygon points="0,472 380,392 380,620 0,620" fill="#1c1c1c"/>
    </svg>

    <div class="holder">
      <p class="holder__name">Colin Warbeck</p>
      <p class="holder__role">Director</p>
      <p class="holder__phone">+61 2 5550 1847</p>
    </div>

    <div class="brand">
      <span class="brand__dot"></span>
      <p class="brand__name">Kestrel Point Wildland Tours</p>
    </div>

    <div class="contact">
      <p>PO Box 71</p>
      <p>Marlin Cove NSW 2471</p>
      <p>info@kestrelpointtours.com</p>
      <p><span class="contact__label">W:</span> www.kestrelpointtours.com</p>
    </div>
  </section>

  <section class="card card--back" aria-label="Business card back">
    <div class="brand">
      <span class="brand__dot"></span>
      <p class="brand__name">Kestrel Point Wildland Tours</p>
    </div>

    <div class="social">
      <div class="social__networks">
        <span>Friendwall</span>
        <span>Pixlane</span>
      </div>
      <p class="social__handle">kpwildtours</p>
    </div>
  </section>

</body>
</html>
```